Business cards and letterhead
UK size business cards/letterhead
Project: Business cards and letterhead
Business cards and letterhead - Information Technology
Creative Brief
Professional
Gareth Pellow
Director
148 Ashcombe Lane Twickenham Middlesex TW4 3QR
gareth.pellow@corvalisen.com
www.corvalisen.com
Note business card needs to be UK-sized (i.e. 85 x 55)/double sided, and the letterhead suitable for A4 paper Back of card can contain some/all of suggested text, depending upon how well it fits
ECM Consultancy Services - Project Management and Delivery - Implementation Planning - Data Conversion Management - Existing System Reviews - Software Design and Development - Test Strategy Definition and Execution

```html
<!DOCTYPE html>
<html lang="en">
<head>
<meta charset="utf-8">
<title>Corvalisen business cards</title>
<link href="https://fonts.googleapis.com/css2?family=Open+Sans:wght@400;600;700&family=Cinzel:wght@400&display=swap" rel="stylesheet">
<style>
  :root {
    --stage: #e9e4dc;
    --card-light: #ffffff;
    --card-dark: #1e1e20;
    --accent: #1d8fc4;
    --accent-deep: #0f6e9c;
    --silver: #b8bcc2;
    --grey-text: #6b6f74;
    --dark-text: #333638;
    --light-text: #d9dbde;
    --label: #3a3632;
  }
  * { margin: 0; padding: 0; box-sizing: border-box; }
  html, body { width: 1200px; height: 794px; overflow: hidden; }
  body {
    background: var(--stage);
    font-family: "Open Sans", Arial, sans-serif;
    position: relative;
  }
  .card {
    position: absolute;
    width: 494px;
    height: 276px;
    border-radius: 14px;
    overflow: hidden;
    box-shadow: 0 3px 8px rgba(0,0,0,0.25);
  }
  .card--light { background: var(--card-light); color: var(--dark-text); }
  .card--dark { background: var(--card-dark); color: var(--light-text); }
  .front-a { left: 72px; top: 38px; }
  .front-b { left: 636px; top: 38px; }
  .back-a { left: 72px; top: 470px; }
  .back-b { left: 636px; top: 470px; }
  .corner-art { position: absolute; inset: 0; width: 494px; height: 276px; }

  .brand {
    position: absolute; left: 22px; top: 150px; width: 210px;
    display: flex; align-items: center; gap: 10px;
  }
  .brand-dot { width: 18px; height: 18px; border-radius: 50%; background: var(--accent); flex: none; }
  .brand-name { font-weight: 700; font-size: 25px; letter-spacing: 1px; }
  .card--light .brand-name { color: #3b3e42; }
  .card--dark .brand-name { color: var(--silver); }

  .divider { position: absolute; left: 244px; top: 42px; width: 1px; height: 190px; background: #c9ccd0; }
  .card--dark .divider { background: #55585c; }

  .contact { position: absolute; left: 258px; top: 40px; width: 220px; }
  .contact-name { color: var(--accent); font-weight: 600; font-size: 15px; line-height: 18px; }
  .contact-role { font-size: 11px; color: var(--grey-text); margin-bottom: 22px; }
  .card--dark .contact-role { color: #a6a9ad; }
  .contact-line { display: flex; gap: 7px; font-size: 10.5px; line-height: 15px; margin-bottom: 6px; }
  .card--light .contact-line { color: var(--dark-text); }
  .contact-icon { width: 10px; height: 10px; flex: none; margin-top: 2px; fill: var(--grey-text); }
  .card--dark .contact-icon { fill: #a6a9ad; }

  .services { position: absolute; left: 32px; top: 80px; }
  .services-title { color: var(--accent); font-size: 17px; font-weight: 600; margin-bottom: 10px; }
  .services-list { list-style: none; }
  .services-list li { font-size: 12px; line-height: 20px; display: flex; align-items: center; gap: 10px; }
  .services-list li::before { content: ""; width: 6px; height: 6px; border-radius: 50%; background: var(--accent); }
  .card--light .services-list li { color: var(--dark-text); }

  .caption {
    position: absolute; width: 494px; text-align: center;
    font-family: "Cinzel", Georgia, serif; font-size: 22px; letter-spacing: 2px; color: var(--label);
  }
  .caption-front-a { left: 72px; top: 340px; }
  .caption-front-b { left: 636px; top: 340px; }
  .caption-back-a { left: 72px; top: 758px; }
  .caption-back-b { left: 636px; top: 758px; }
</style>
</head>
<body>

<svg width="0" height="0" style="position:absolute">
  <defs>
    <symbol id="corner-accents" viewBox="0 0 494 276">
      <path d="M400 0 H494 V70 Q470 20 400 0 Z" fill="var(--accent)"/>
      <path d="M385 0 Q470 18 494 85 V70 Q470 20 400 0 Z" fill="var(--silver)"/>
      <path d="M0 190 Q30 255 110 276 H0 Z" fill="var(--accent)"/>
      <path d="M0 175 Q30 250 125 276 H110 Q30 255 0 190 Z" fill="var(--silver)"/>
    </symbol>
    <symbol id="icon-pin" viewBox="0 0 10 10"><path d="M5 0 A3.5 3.5 0 0 1 8.5 3.5 C8.5 6 5 10 5 10 C5 10 1.5 6 1.5 3.5 A3.5 3.5 0 0 1 5 0 Z M5 2 A1.5 1.5 0 1 0 5 5 A1.5 1.5 0 1 0 5 2 Z"/></symbol>
    <symbol id="icon-phone" viewBox="0 0 10 10"><path d="M2 0 L4 2.5 L3 3.7 Q4.2 6 6.3 7 L7.5 6 L10 8 L8.5 10 Q3 9 0 1.5 Z"/></symbol>
    <symbol id="icon-mail" viewBox="0 0 10 10"><path d="M0 2 H10 V8 H0 Z M0.8 2.6 L5 5.6 L9.2 2.6 V2.9 L5 6.2 L0.8 2.9 Z"/></symbol>
    <symbol id="icon-web" viewBox="0 0 10 10"><path d="M5 0 A5 5 0 1 0 5 10 A5 5 0 1 0 5 0 Z M5 1.2 A3.8 3.8 0 1 1 5 8.8 A3.8 3.8 0 1 1 5 1.2 Z"/></symbol>
  </defs>
</svg>

<section class="card card--light front-a">
  <svg class="corner-art" aria-hidden="true"><use href="#corner-accents"/></svg>
  <div class="brand"><span class="brand-dot"></span><span class="brand-name">CORVALISEN</span></div>
  <div class="divider"></div>
  <div class="contact">
    <p class="contact-name">Gareth Pellow</p>
    <p class="contact-role">Director</p>
    <p class="contact-line"><svg class="contact-icon"><use href="#icon-pin"/></svg><span>148 Ashcombe Lane Twickenham<br>Middlesex TW4 3QR</span></p>
    <p class="contact-line"><svg class="contact-icon"><use href="#icon-phone"/></svg><span>+44-7700-900-418</span></p>
    <p class="contact-line"><svg class="contact-icon"><use href="#icon-mail"/></svg><span>gareth.pellow@corvalisen.com</span></p>
    <p class="contact-line"><svg class="contact-icon"><use href="#icon-web"/></svg><span>www.corvalisen.com</span></p>
  </div>
</section>

<section class="card card--dark front-b">
  <svg class="corner-art" aria-hidden="true"><use href="#corner-accents"/></svg>
  <div class="brand"><span class="brand-dot"></span><span class="brand-name">CORVALISEN</span></div>
  <div class="divider"></div>
  <div class="contact">
    <p class="contact-name">Gareth Pellow</p>
    <p class="contact-role">Director</p>
    <p class="contact-line"><svg class="contact-icon"><use href="#icon-pin"/></svg><span>148 Ashcombe Lane Twickenham<br>Middlesex TW4 3QR</span></p>
    <p class="contact-line"><svg class="contact-icon"><use href="#icon-phone"/></svg><span>+44-7700-900-418</span></p>
    <p class="contact-line"><svg class="contact-icon"><use href="#icon-mail"/></svg><span>gareth.pellow@corvalisen.com</span></p>
    <p class="contact-line"><svg class="contact-icon"><use href="#icon-web"/></svg><span>www.corvalisen.com</span></p>
  </div>
</section>

<section class="card card--light back-a">
  <div class="services">
    <h2 class="services-title">ECM Consultancy Services</h2>
    <ul class="services-list">
      <li>Project Management and Delivery</li>
      <li>Implementation Planning</li>
      <li>Data Conversion Management</li>
      <li>Existing System Reviews</li>
      <li>Software Design and Development</li>
      <li>Test Strategy Definition and Execution</li>
    </ul>
  </div>
</section>

<section class="card card--dark back-b">
  <div class="services">
    <h2 class="services-title">ECM Consultancy Services</h2>
    <ul class="services-list">
      <li>Project Management and Delivery</li>
      <li>Implementation Planning</li>
      <li>Data Conversion Management</li>
      <li>Existing System Reviews</li>
      <li>Software Design and Development</li>
      <li>Test Strategy Definition and Execution</li>
    </ul>
  </div>
</section>

<p class="caption caption-front-a">Business Card Front A</p>
<p class="caption caption-front-b">Business Card Front B</p>
<p class="caption caption-back-a">Business Card Back A</p>
<p class="caption caption-back-b">Business Card Back B</p>

</body>
</html>
```